Industrial Professional Business Card Design (Vantrel Systems)

Would like professional looking business cards. Not too busy leaning towards minimal. Should have a slogan like:
"Industrial Automation and Control".

We are a tech company that programs industrial PLC computers. We also develop custom hardware solutions. Please use the logo for inspiration.

Target Market(s)

Mining, industrial, processing, automation, factory

Industry/Entity Type

Engineering

Contact Information for Business Card

Name, phone, email, website. job title.

Font styles to use
Other font styles liked:
• droid sans

Requirements
Must have
• Use colours that go well with the logo. Not too busy design.

```html
<!DOCTYPE html>
<html lang="en">
<head>
<meta charset="utf-8">
<title>Vantrel Systems — Business Card</title>
<link href="https://fonts.googleapis.com/css2?family=Open+Sans:wght@400;700&display=swap" rel="stylesheet">
<style>
  :root {
    --navy: #1f4e79;
    --orange: #f07023;
    --ink: #555a60;
    --paper: #ffffff;
    --backdrop: #e9eaeb;
  }
  * { margin: 0; padding: 0; box-sizing: border-box; }
  html, body { width: 1200px; height: 900px; overflow: hidden; }
  body {
    background: var(--backdrop);
    font-family: "Open Sans", sans-serif;
    display: flex;
    align-items: center;
    justify-content: center;
    gap: 40px;
  }
  .card {
    position: relative;
    width: 540px;
    height: 309px;
    background: var(--paper);
    box-shadow: 0 6px 18px rgba(0,0,0,0.12);
  }
  .brand {
    display: flex;
    align-items: center;
    gap: 10px;
    color: var(--navy);
    font-weight: 400;
    white-space: nowrap;
  }
  .brand-dot {
    border-radius: 50%;
    background: var(--orange);
    flex: none;
  }
  .card-front { display: flex; align-items: center; justify-content: center; }
  .card-front .brand { font-size: 38px; }
  .card-front .brand-dot { width: 26px; height: 26px; }

  .card-back .brand {
    position: absolute;
    top: 48px;
    right: 36px;
    font-size: 24px;
  }
  .card-back .brand-dot { width: 16px; height: 16px; }
  .divider {
    position: absolute;
    left: 36px;
    right: 36px;
    top: 170px;
    height: 1.5px;
    background: var(--orange);
  }
  .person {
    position: absolute;
    left: 36px;
    bottom: 146px;
  }
  .person-name {
    color: var(--navy);
    font-weight: 700;
    font-size: 19px;
    letter-spacing: 0.5px;
    line-height: 1.1;
  }
  .person-title {
    color: var(--ink);
    font-size: 13px;
  }
  .contact-list {
    position: absolute;
    left: 36px;
    top: 184px;
    list-style: none;
    color: var(--ink);
    font-size: 12.5px;
    line-height: 1.55;
  }
  .contact-list li { display: flex; align-items: center; gap: 8px; }
  .contact-list svg { width: 11px; height: 11px; fill: var(--navy); flex: none; }
  .address {
    position: absolute;
    right: 36px;
    top: 184px;
    text-align: right;
    color: var(--ink);
    font-size: 12.5px;
    line-height: 1.55;
  }
</style>
</head>
<body>
  <section class="card card-front">
    <div class="brand"><span class="brand-dot"></span>Vantrel Systems</div>
  </section>

  <section class="card card-back">
    <div class="brand"><span class="brand-dot"></span>Vantrel Systems</div>

    <div class="person">
      <p class="person-name">DALEN HARTLEY</p>
      <p class="person-title">Owner/CEO</p>
    </div>

    <div class="divider"></div>

    <ul class="contact-list">
      <li>
        <svg viewBox="0 0 24 24" aria-hidden="true"><path d="M6.6 10.8a15.1 15.1 0 0 0 6.6 6.6l2.2-2.2c.3-.3.7-.4 1-.2 1.1.4 2.3.6 3.6.6.6 0 1 .4 1 1V20c0 .6-.4 1-1 1A17 17 0 0 1 3 4c0-.6.4-1 1-1h3.5c.6 0 1 .4 1 1 0 1.3.2 2.5.6 3.6.1.3 0 .7-.2 1z"/></svg>
        (555) 610-2847
      </li>
      <li>
        <svg viewBox="0 0 24 24" aria-hidden="true"><path d="M3 9c0-3 4-5 9-5s9 2 9 5v2h-5V8.5c-2-.7-6-.7-8 0V11H3zM6 12h12l2 8H4z"/></svg>
        (555) 610-3390 ext 118
      </li>
      <li>
        <svg viewBox="0 0 24 24" aria-hidden="true"><path d="M2 5h20v14H2zm2 2v.5l8 5 8-5V7z"/></svg>
        dalen@vantrelsystems.com
      </li>
      <li>
        <svg viewBox="0 0 24 24" aria-hidden="true"><circle cx="12" cy="12" r="10"/></svg>
        www.vantrelsystems.com
      </li>
    </ul>

    <address class="address" style="font-style: normal;">
      210 - 4821 Harlow<br>
      Ave Brennick, BC V2K4M7
    </address>
  </section>
</body>
</html>
```